Banner Ad for website hompage - Design Project

We need 4 banner ads for the homepage of a Rent a Car company based in dubai. We rent a wide range of cars but mainly deal in the affordable cars category. Our website colors are mainly red, white and black and I can send pictures of the website (attached) if you want something to compare possible design ideas with. The banners need to promote different messages and must be appealing to the end user. It must also use pictures of cars that exist in our fleet (Pls note: this is only if you are using cars in the banner ad)

The 4 banner ads needed are as follows:
1) should promote something along the lines of we have 20+ models available and reserve a car now (This banner should also have a reserve now button, not the actual button but it's design. The button will be made and coded by us)
2) should promote something along the lines of we offer personalised service and we look after each and every custoemr individually
3) we provide attractive rates based on daily, weekly, monthly and longer rental periods (should also incorporate a reserve now message)
4) Like us on quorvia and follow us on social media for additional offers and discounts (would like for this to have a like button design implemented in it which will be linked to quorvia.)

Also please not the picture file size is 940pixels by 400pixels

Finally: I also need the psd files for the banners.

```html
<!DOCTYPE html>
<html lang="en">
<head>
<meta charset="utf-8">
<title>Quorvia Social Offers Banner</title>
<link rel="stylesheet" href="https://fonts.googleapis.com/css2?family=Oswald:wght@400&display=swap">
<style>
  :root {
    --ink-deep: #050505;
    --ground-mid: #6e6e6e;
    --ground-light: #c9c9c9;
    --headline: #f4f4f4;
    --button-face: #eef1f7;
    --button-edge: #b9c3d8;
    --button-text: #3b4a6b;
    --button-mark: #3b5998;
  }
  html, body {
    margin: 0;
    padding: 0;
    width: 1200px;
    height: 511px;
    overflow: hidden;
    background: var(--ink-deep);
  }
  .banner {
    position: relative;
    width: 1200px;
    height: 511px;
    overflow: hidden;
  }
  .banner-backdrop {
    position: absolute;
    inset: 0;
    background:
      radial-gradient(ellipse 420px 260px at 640px 440px, var(--ground-light) 0%, rgba(160,160,160,0.6) 45%, rgba(0,0,0,0) 100%),
      radial-gradient(ellipse 300px 200px at 1080px 380px, rgba(150,150,150,0.55) 0%, rgba(0,0,0,0) 100%),
      radial-gradient(ellipse 260px 160px at 120px 200px, rgba(120,120,120,0.45) 0%, rgba(0,0,0,0) 100%),
      linear-gradient(180deg, #1a1a1a 0%, var(--ground-mid) 55%, #3a3a3a 100%);
  }
  .banner-shade {
    position: absolute;
    inset: 0;
    background:
      radial-gradient(ellipse 520px 200px at 560px 60px, rgba(0,0,0,0.85) 0%, rgba(0,0,0,0) 100%),
      linear-gradient(90deg, rgba(0,0,0,0.55) 0%, rgba(0,0,0,0) 30%, rgba(0,0,0,0) 75%, rgba(0,0,0,0.45) 100%);
  }
  .headline {
    position: absolute;
    left: 315px;
    top: 183px;
    width: 843px;
    margin: 0;
    font-family: "Oswald", "Arial Narrow", sans-serif;
    font-weight: 400;
    font-size: 55px;
    line-height: 75px;
    color: var(--headline);
    text-transform: uppercase;
    text-shadow: 0 1px 3px rgba(0,0,0,0.6);
    transform: scaleX(0.82);
    transform-origin: left top;
  }
  .headline-line {
    display: block;
    text-align: justify;
    text-align-last: justify;
    white-space: nowrap;
  }
  .headline-line--last {
    text-align: left;
    text-align-last: left;
    padding-left: 262px;
  }
  .like-button {
    position: absolute;
    left: 818px;
    top: 354px;
    width: 62px;
    height: 26px;
    box-sizing: border-box;
    display: flex;
    align-items: center;
    gap: 6px;
    padding: 0 6px;
    background: var(--button-face);
    border: 1px solid var(--button-edge);
    border-radius: 3px;
    font-family: "Oswald", "Arial Narrow", sans-serif;
    font-size: 14px;
    color: var(--button-text);
  }
  .like-button-mark {
    width: 14px;
    height: 14px;
    background: var(--button-mark);
    border-radius: 2px;
  }
</style>
</head>
<body>
  <div class="banner">
    <div class="banner-backdrop" role="img" aria-label="Dark monochrome photograph of cracked dry ground under shadowy spiky leaves"></div>
    <div class="banner-shade"></div>
    <h1 class="headline">
      <span class="headline-line">Like us on quorvia and follow us on</span>
      <span class="headline-line">Social media for additional offers</span>
      <span class="headline-line headline-line--last">and discounts</span>
    </h1>
    <div class="like-button"><span class="like-button-mark"></span>Like</div>
  </div>
</body>
</html>
```